Wine Can for New StartUp Winery (Golden Heron Sangría)

Hello everyone! After years of crafting the perfect sangría, we’re thrilled to launch it in a can for the first time. We’re looking to create a premium, elegant design that reflects the high quality and deliciousness of our beloved drink. Can you help us design the can everyone will love?

We encourage your creativity, so have fun with it! There are just a few guidelines:

NAME: GOLDEN HERON SANGRÍA
LOGO: Bull
PRODUCT: Wine, Sangría Española
COLOR: Primary colors are red and white
DIMENSIONS: 250ml can
STYLE: Elegant, modern, sophisticated, misty
INFORMATION: Live space for the ingredients, % alcohol, country
CAN MATERIAL: The material is alumium (ensure that the print will match the colors)
KEEP IN MIND: Premium

Places to help you with some ideas:
Web Page: https://www.velortacasa.com.au/sangria/
Instagram: https://www.instagram.com/goldenheronsangria/

Target Market(s)

Wine lovers

Industry/Entity Type

Winery

Colors
EB3D1F
EC4F4E
F09395
F8D3D4
FCEDEE

Requirements
Must have
• The logo, the signature of Tobías, the bull
Nice to have
• Big bull, wine motion liquid, misty effect as cold
Should not have
• So many icons or figures

```html
<!DOCTYPE html>
<html lang="en">
<head>
<meta charset="utf-8">
<title>Golden Heron Sangría – Can Label</title>
<link href="https://fonts.googleapis.com/css2?family=Poppins:wght@400;500;700&display=swap" rel="stylesheet">
<style>
  :root {
    --page: #f7f9fc;
    --red-top: #df2330;
    --red-bottom: #b02b34;
    --stripe-red: #d42a33;
    --white: #ffffff;
  }
  * { margin: 0; padding: 0; box-sizing: border-box; }
  html, body {
    width: 703px; height: 1200px; overflow: hidden;
    background: var(--page);
    font-family: "Poppins", sans-serif;
    color: var(--white);
  }
  .label {
    position: absolute; left: 38px; top: 359px;
    width: 627px; height: 482px;
  }
  .stripes { position: absolute; left: 0; width: 100%; }
  .stripes--top {
    top: 0; height: 21px;
    background: linear-gradient(to bottom,
      var(--stripe-red) 0 7px, var(--white) 7px 10px,
      var(--stripe-red) 10px 15px, var(--white) 15px 21px);
  }
  .stripes--bottom {
    bottom: 0; height: 18px;
    background: linear-gradient(to bottom,
      var(--white) 0 6px, var(--stripe-red) 6px 11px,
      var(--white) 11px 14px, var(--stripe-red) 14px 18px);
  }
  .panel {
    position: absolute; left: 0; top: 21px; width: 100%; height: 443px;
    overflow: hidden;
    background: linear-gradient(172deg, var(--red-top) 0%, #c92831 45%, var(--red-bottom) 100%);
  }
  .brand {
    position: absolute; left: 90px; top: 60px; width: 240px;
    text-align: center;
  }
  .brand-mark {
    width: 80px; height: 80px; margin: 0 auto 32px;
    border: 2px solid var(--white); border-radius: 50%;
  }
  .brand-name {
    font-weight: 700; font-size: 22px; line-height: 23px; letter-spacing: 0.2px;
    white-space: nowrap;
  }
  .product {
    position: absolute; left: 113px; top: 292px; width: 194px;
    text-align: center;
    font-weight: 400; font-size: 21px; line-height: 30px;
    padding-bottom: 6px;
    border-bottom: 2px solid var(--white);
    white-space: nowrap;
  }
  .volume {
    position: absolute; left: 169px; top: 375px; width: 80px; height: 68px;
    border: 1.5px solid var(--white); border-bottom: none;
    border-radius: 6px 6px 0 0;
    padding: 3px 3px 0;
  }
  .volume-inner {
    height: 100%;
    border: 1.5px solid var(--white); border-bottom: none;
    border-radius: 4px 4px 0 0;
    text-align: center; font-size: 14px; line-height: 18px;
    padding: 5px 5px 0;
  }
  .volume-inner .size { padding-bottom: 5px; border-bottom: 1.5px solid var(--white); }
  .volume-inner .abv { padding-top: 6px; font-size: 13.5px; letter-spacing: -0.3px; white-space: nowrap; }
  .ingredients {
    position: absolute; left: 444px; top: 61px; width: 158px; height: 344px;
    border: 2px solid var(--white);
    text-align: center;
  }
  .ingredients h2 {
    font-weight: 500; font-size: 19.5px; line-height: 24px; margin-top: 6px;
    letter-spacing: 0.2px;
  }
</style>
</head>
<body>
  <section class="label" aria-label="Golden Heron Sangría can label">
    <div class="stripes stripes--top"></div>
    <div class="panel">
      <div class="brand">
        <div class="brand-mark"></div>
        <h1 class="brand-name">GOLDEN HERON<br>SANGRÍA</h1>
      </div>
      <p class="product">Sangría Española</p>
      <div class="volume">
        <div class="volume-inner">
          <div class="size">250 ml</div>
          <div class="abv">ALC 20%</div>
        </div>
      </div>
      <div class="ingredients">
        <h2>INGREDIENTS</h2>
      </div>
    </div>
    <div class="stripes stripes--bottom"></div>
  </section>
</body>
</html>
```